456Fetesound

We only need one indexpage mockup design.

a redesign for our current page which you can see on www.brightfete.co.uk

I have made a very good video here that explains:
http://www.vidloom.example/watch?v=qTrLw8pZ2Xa

And this one which goes through the content: http://www.vidloom.example/watch?v=hNdWz3vRbue

We help people find bands, DJ and solomusicians for their events.
The goal is to make them create a free enquiry.
The company has been runing since 2005 and the simple, easy webpage has worked very good for us, so dont make it too fancy
Updates

Reason: Sorry. I have set a wrong deadline

Target Market(s)

People from northern Europe, between 29 and 55
PLanning the event of their lifetime - big wedding or big birthday.
Looking for great live musicians who can make their event great

Industry/Entity Type

It Company

Requirements
Must have
• Simplicity and great usability
Nice to have
• Watch the video:http://www.vidloom.example/watch?v=hNdWz3vRbue
Should not have
• - NO Fancy colours
- Should NOT only be focused on Young pepople, but also target the older
- Not too dark colours

```html
<!DOCTYPE html>
<html lang="en">
<head>
<meta charset="utf-8">
<title>456Fetesound – Find bands, DJs and solo musicians</title>
<link rel="stylesheet" href="https://fonts.googleapis.com/css2?family=Fredoka:wght@500;600&family=Source+Sans+3:wght@300;400;600&family=Arimo:wght@400&display=swap">
<style>
:root{
  --orange:#f26b35;
  --orange-light:#ff8a55;
  --orange-dark:#e2571f;
  --grey-text:#555;
  --grey-mid:#8d8d8d;
  --grey-frame:#a4a4a4;
  --page:#f1f1f1;
  --white:#fff;
  --footer-top:#6e6e6e;
  --footer-bottom:#4b4b4b;
  --body-text:#444;
}
*{box-sizing:border-box;margin:0;padding:0}
html,body{width:1197px;height:1200px;overflow:hidden;background:var(--page)}
body{position:relative;font-family:"Arimo",Arial,sans-serif;color:var(--body-text)}
.abs{position:absolute}

/* header */
.site-header{left:0;top:0;width:1197px;height:130px;background:linear-gradient(#f9f9f9,#e6e6e6);border-top:4px solid #dcdcdc}
.brand{left:74px;top:22px;display:flex;align-items:center;gap:14px}
.brand-dot{width:82px;height:82px;border-radius:50%;background:var(--orange)}
.brand-name{font-family:"Source Sans 3",sans-serif;font-weight:400;font-size:36px;color:var(--grey-mid);letter-spacing:.5px}
.login{left:832px;top:0;width:292px;height:41px;background:#d4d4d4;border-radius:0 0 8px 8px;display:flex;align-items:center;gap:12px;padding:0 10px}
.login input{width:100px;height:20px;border:1px solid #c6c6c6;font:11px "Arimo",sans-serif;padding:0 5px;color:#999}
.login button{height:20px;padding:0 6px;border:0;background:var(--orange);color:var(--white);font:12px "Source Sans 3",sans-serif}
.main-nav{left:831px;top:79px;display:flex;gap:8px;font-family:"Source Sans 3",sans-serif;font-size:15px}
.main-nav a{display:block;height:32px;line-height:32px;padding:0 10px;color:var(--grey-mid);text-decoration:none}
.main-nav a + a{margin-left:18px}
.main-nav a.is-active{background:linear-gradient(#9a9a9a,#777);color:var(--white);border-radius:4px}

/* hero */
.hero{left:0;top:130px;width:1197px;height:283px;background:linear-gradient(var(--orange-light),var(--orange) 60%,#f87440)}
.hero-title{left:0;top:8px;width:1197px;text-align:center;font-family:"Fredoka",sans-serif;font-weight:600;font-size:25px;line-height:25px;color:var(--white);text-shadow:0 1px 2px rgba(0,0,0,.35)}
.step-card{top:81px;width:170px;height:188px;background:linear-gradient(#fff,#e4e4e4);padding:10px 14px}
.step-card h3{font-family:"Source Sans 3",sans-serif;font-weight:400;font-size:15px;line-height:17px;color:var(--orange);height:40px}
.step-card p{font-size:13px;line-height:20px;color:var(--grey-text);text-align:center;margin-top:4px}
.step-card .icon{position:absolute;left:60px;bottom:10px;width:52px;height:48px;border-radius:4px}
.step-card .fold{position:absolute;right:0;top:0}
.kind-title{left:613px;top:116px;font-family:"Fredoka",sans-serif;font-weight:500;font-size:20px;color:var(--white);text-shadow:0 1px 2px rgba(0,0,0,.25)}
.kind-tile{top:154px;width:167px;height:115px;border:2px solid var(--white);border-radius:6px;overflow:hidden}
.kind-tile .photo{position:absolute;inset:0}
.kind-tile span{position:absolute;left:8px;bottom:4px;font-family:"Fredoka",sans-serif;font-weight:500;font-size:22px;color:var(--white)}

/* features */
.feature{top:423px;width:299px}
.feature h2{display:flex;align-items:center;gap:8px;height:44px;font-family:"Source Sans 3",sans-serif;font-weight:300;font-size:23px;color:var(--grey-text)}
.feature h2::before{content:"";width:30px;height:30px;border-radius:50%;background:#b9b9b9}
.feature p{font-size:13px;line-height:19.5px;color:var(--grey-text);text-align:justify}
.feature .lead{height:40px;margin-top:4px}
.feature .frame{margin-top:10px;width:295px;height:135px;background:var(--grey-frame);padding:7px 8px}
.feature .frame div{width:100%;height:100%;border:1px solid var(--white)}
.feature .frame + p{margin-top:18px;height:78px}
.readmore{display:block;margin-left:auto;margin-top:14px;width:84px;height:23px;border-radius:4px;background:linear-gradient(var(--orange-light),var(--orange-dark));color:var(--white);font-family:"Source Sans 3",sans-serif;font-size:13px;text-align:center;line-height:23px;text-decoration:none}
.divider{top:473px;width:1px;height:240px;background:#cfcfcf}

/* recommendation */
.recommend{left:169px;top:817px;width:848px;height:111px;border:5px solid #8f8f8f;background:var(--white)}
.recommend .shot{position:absolute;left:3px;top:3px;width:280px;height:95px;background:linear-gradient(90deg,#b8c4a2,#e8ece0 70%,#fff)}
.recommend p{position:absolute;left:290px;top:16px;width:500px;font-family:"Source Sans 3",sans-serif;font-size:22px;line-height:32px;color:var(--grey-text);white-space:nowrap}
.recommend strong{color:var(--orange);font-weight:600}
.recommend em{font-style:normal;color:var(--orange)}

/* footer */
.site-footer{left:0;top:953px;width:1197px;height:247px;background:linear-gradient(var(--footer-top),var(--footer-bottom));border-top:3px dotted #9a9a9a}
.site-footer h2{position:absolute;left:78px;top:20px;font-family:"Source Sans 3",sans-serif;font-weight:400;font-size:22px;color:var(--white)}
.enq-col{top:70px}
.enq-col h3{font-family:"Source Sans 3",sans-serif;font-weight:600;font-size:15px;color:var(--white);margin-bottom:8px}
.enq-col ul{list-style:none}
.enq-col li{position:relative;padding-left:19px;font-size:13px;line-height:26px;color:var(--white)}
.enq-col li::before{content:"";position:absolute;left:2px;top:10px;width:7px;height:7px;border-radius:50%;background:var(--orange)}
.foot-brand{left:914px;top:196px;display:flex;align-items:center;gap:8px}
.foot-brand i{width:20px;height:20px;border-radius:50%;background:var(--orange)}
.foot-brand span{font-family:"Source Sans 3",sans-serif;font-size:26px;color:var(--white)}
</style>
</head>
<body>

<header class="site-header abs">
  <div class="brand abs"><div class="brand-dot"></div><span class="brand-name">456Fetesound</span></div>
  <form class="login abs"><input value="username"><input value="password"><button type="button">Login</button></form>
  <nav class="main-nav abs"><a class="is-active" href="#">About</a><a href="#">Find Enquiry</a><a href="#">New Artist</a></nav>
</header>

<section class="hero abs">
  <h1 class="hero-title abs">2500 bands, DJs and solomusicions are realy to send you offers<br>on your next event</h1>

  <article class="step-card abs" style="left:58px">
    <svg class="fold" width="40" height="40"><path d="M0 0H40V40C34 22 20 6 0 0Z" fill="#d8d8d8"/></svg>
    <h3>Free<br>Enquery</h3><p>Lorem ipsum dolor sit amet, consectetuer adipiscing elit.</p>
    <div class="icon" role="img" aria-label="Notepad and pencil icon" style="background:linear-gradient(#e9eef8,#b8c6de)"></div>
  </article>
  <article class="step-card abs" style="left:238px">
    <svg class="fold" width="40" height="40"><path d="M0 0H40V40C34 22 20 6 0 0Z" fill="#d8d8d8"/></svg>
    <h3>Get Some<br>offers</h3><p>Lorem ipsum dolor sit amet, consectetuer adipiscing elit.</p>
    <div class="icon" role="img" aria-label="Envelope with offer cards icon" style="background:linear-gradient(#8fc6e8,#f2a04a)"></div>
  </article>
  <article class="step-card abs" style="left:419px">
    <svg class="fold" width="40" height="40"><path d="M0 0H40V40C34 22 20 6 0 0Z" fill="#d8d8d8"/></svg>
    <h3>Chose Musician<br>Looking For</h3><p>Lorem ipsum dolor sit amet, consectetuer adipiscing elit.</p>
    <div class="icon" role="img" aria-label="Electric guitar icon" style="background:linear-gradient(#c9c9c9,#7a4a3a)"></div>
  </article>

  <h2 class="kind-title abs">Which kind of party music are you looking for?</h2>
  <a class="kind-tile abs" style="left:613px" href="#"><div class="photo" role="img" aria-label="Black and white photo of a four-piece band on stage" style="background:linear-gradient(#e8e8e8 0,#8a8a8a 55%,var(--orange) 70%,var(--orange-dark))"></div><span>Bands</span></a>
  <a class="kind-tile abs" style="left:789px" href="#"><div class="photo" role="img" aria-label="DJ at a mixing desk" style="background:linear-gradient(#7a2a3a 0,#3a1a2a 55%,#2a2a2a 70%,#111)"></div><span>DJs</span></a>
  <a class="kind-tile abs" style="left:966px" href="#"><div class="photo" role="img" aria-label="Three electric guitars on stands" style="background:linear-gradient(#f2f2f2 0,#5a5a5a 55%,#2a2a2a 70%,#111)"></div><span>Solo</span></a>
</section>

<section class="feature abs" style="left:71px">
  <h2>Satisfaction</h2>
  <p class="lead">Lorem ipsum dolor sit amet, consectetuer adipi-scing elit.</p>
  <div class="frame"><div role="img" aria-label="Smiling man in a shirt and tie talking on a phone" style="background:linear-gradient(90deg,#3d4f3a,#d9dfd6 50%,#556b4f)"></div></div>
  <p>Lorem ipsum dolor sit amet, consectetuer adipi-scing elit. Nam nibh. Nunc varius facilisis eros. Sed erat. In in velit quis arcu ornare laoreet. Curabitur adipiscing luctus massa.</p>
  <a class="readmore" href="#">Readmore</a>
</section>
<div class="divider abs" style="left:411px"></div>
<section class="feature abs" style="left:450px">
  <h2>Biggest in denmark</h2>
  <p class="lead">Lorem ipsum dolor sit amet, consectetuer adipi-scing elit.</p>
  <div class="frame"><div role="img" aria-label="Large outdoor festival stage with crowd at dusk" style="background:linear-gradient(#6a7f99,#8a5a3a 45%,#2a2418)"></div></div>
  <p>Lorem ipsum dolor sit amet, consectetuer adipi-scing elit. Nam nibh. Nunc varius facilisis eros. Sed erat. In in velit quis arcu ornare laoreet. Curabitur adipiscing luctus massa.</p>
  <a class="readmore" href="#">Readmore</a>
</section>
<div class="divider abs" style="left:784px"></div>
<section class="feature abs" style="left:823px">
  <h2>24 hours</h2>
  <p class="lead">Lorem ipsum dolor sit amet, consectetuer adipi-scing elit.</p>
  <div class="frame"><div role="img" aria-label="DJ playing to a packed club under purple lights" style="background:linear-gradient(#5a3ab0,#8a4ac8 40%,#2a1640 75%,#c0203a)"></div></div>
  <p>Lorem ipsum dolor sit amet, consectetuer adipi-scing elit. Nam nibh. Nunc varius facilisis eros. Sed erat. In in velit quis arcu ornare laoreet. Curabitur adipiscing luctus massa.</p>
  <a class="readmore" href="#">Readmore</a>
</section>

<aside class="recommend abs">
  <div class="shot" role="img" aria-label="Screenshot of the Bargainhour consumer programme web page"></div>
  <p><strong>456 fetesound</strong> has been recommended on <strong>NRs</strong><br><strong>bargainhour</strong> under ourold name <em>Allyourfete.example</em></p>
  <svg class="abs" style="right:0;top:0" width="44" height="44"><path d="M0 0H44V44C38 24 22 6 0 0Z" fill="#d8d8d8"/></svg>
</aside>

<footer class="site-footer abs">
  <h2>Newest enquiries</h2>
  <div class="enq-col abs" style="left:89px"><h3>Musictype</h3><ul><li>Solomusician</li><li>DJ</li><li>Band</li><li>Band</li><li>Band</li></ul></div>
  <div class="enq-col abs" style="left:268px"><h3>City</h3><ul><li>Chandigar</li><li>New Delphi</li><li>Athens</li><li>Athens</li><li>Athens</li></ul></div>
  <div class="enq-col abs" style="left:465px"><h3>Festtype</h3><ul><li>Birthday</li><li>Weddings</li><li>Companys</li><li>Companys</li><li>Companys</li></ul></div>
  <div class="enq-col abs" style="left:645px"><h3>Area</h3><ul><li>Northindia</li><li>central</li><li>Greese</li><li>Greese</li><li>Greese</li></ul></div>
  <div class="enq-col abs" style="left:801px"><h3>Musictype</h3><ul><li>45</li><li>200</li><li>150</li><li>20</li><li>15</li></ul></div>
  <div class="foot-brand abs"><i></i><span>456Fetesound</span></div>
</footer>

</body>
</html>
```